New Business Card Design Project

hello again,
i have an awful year and we were not able to complete our logo plan. we would like to use our #1 logo for business card design process. the primary colors for business card should be white background with orange & black letters. our business is mobil truck cranes. we deliver heavy stuff and unload cargo with crane that is mounted on our trucks.
here is our business card info:
HARBOR LIFT HAULERS, INC.
428 WESTCOTT AVE
MERRICK, NY 11542
OFFICE - 516 487 3091
DIRECT - 1 888 LIFT HAULS
MARK@HLHAULERS.COM
PLEASE also try to get our slogan on card .... "Our Loads Keep Rollin"
lastly please also put "24 hour Knuckleboom Service"
you can call me anytime 24/7 to discuss...my cell # is: 516 759 2036
please also list: Mark Delroy, President
Target Market(s)
Heavy Construction industry
Industry/Entity Type
heavy construction industry
Contact Information for Business Card
24 Hr Knuckleboom Service

```html
<!DOCTYPE html>
<html lang="en">
<head>
<meta charset="utf-8">
<title>Harbor Lift Haulers – Business Card</title>
<link rel="stylesheet" href="https://fonts.googleapis.com/css2?family=Lora:wght@400;500&family=Open+Sans:wght@400&display=swap">
<style>
  :root {
    --bg: #8fa3d6;
    --ink: #1b1b1b;
    --black-top: #2e2e2e;
    --black-bottom: #121212;
    --orange: #d07712;
    --white: #ffffff;
    --muted: #3a3a3a;
    --rule: #e2e2e2;
    --serif: "Lora", Georgia, serif;
    --sans: "Open Sans", Arial, sans-serif;
  }
  * { box-sizing: border-box; margin: 0; padding: 0; }
  html, body { width: 1200px; height: 876px; overflow: hidden; }
  body {
    background: var(--bg);
    display: flex;
    align-items: center;
    justify-content: center;
    gap: 40px;
    font-family: var(--serif);
  }
  .card {
    position: relative;
    width: 560px;
    height: 320px;
    overflow: hidden;
    box-shadow: 0 10px 24px rgba(20, 30, 70, .35);
  }
  .accent {
    position: absolute;
    width: 58px;
    height: 30px;
    background: var(--orange);
  }

  /* Front */
  .card--front { background: var(--white); }
  .front__band {
    position: absolute;
    left: 0; top: 0; right: 0;
    height: 140px;
    background: linear-gradient(135deg, var(--black-top), var(--black-bottom));
  }
  .front__band .accent--left { left: 0; bottom: -15px; }
  .front__mark {
    position: absolute;
    top: 26px; right: 40px;
    text-align: left;
    color: var(--white);
  }
  .front__logo {
    font-size: 62px;
    line-height: 1;
    letter-spacing: 1px;
    margin-left: 40px;
  }
  .front__service {
    margin-top: 6px;
    font-size: 16px;
    color: var(--white);
  }
  .front__service .hours {
    color: var(--orange);
    font-size: 30px;
    vertical-align: -4px;
    margin-right: 4px;
  }
  .front__body {
    position: absolute;
    left: 36px; right: 30px; top: 156px;
  }
  .company {
    font-size: 25px;
    color: var(--ink);
    letter-spacing: .5px;
  }
  .company .hl { color: var(--orange); }
  .web {
    font-size: 12px;
    letter-spacing: 7px;
    color: var(--muted);
    margin-top: 4px;
  }
  .contacts {
    display: flex;
    margin-top: 18px;
    font-family: var(--sans);
    font-size: 10px;
    color: var(--muted);
    line-height: 1.5;
  }
  .contacts__col { padding-right: 18px; }
  .contacts__col + .contacts__col {
    padding-left: 18px;
    border-left: 1px solid var(--rule);
  }
  .contacts__row { display: flex; align-items: flex-start; gap: 5px; }
  .contacts__row svg { flex: none; margin-top: 2px; }
  .contacts .phone { font-size: 13px; }
  .card--front .accent--right { right: 0; bottom: 40px; }

  /* Back */
  .card--back {
    background: linear-gradient(125deg, var(--black-top) 0%, #3a3a3a 40%, var(--black-bottom) 100%);
    color: var(--white);
  }
  .card--back .accent--left { left: 0; top: 60px; }
  .card--back .accent--right { right: 0; bottom: 60px; }
  .back__content {
    position: absolute;
    inset: 0;
    display: flex;
    flex-direction: column;
    align-items: center;
    justify-content: center;
  }
  .back__logo {
    font-size: 84px;
    line-height: 1;
    letter-spacing: 2px;
  }
  .slogan {
    margin-top: 10px;
    font-size: 22px;
    letter-spacing: .5px;
  }
  .slogan .hl { color: var(--orange); }
  .card--back .web { color: var(--white); margin-top: 8px; }
</style>
</head>
<body>

  <section class="card card--front" aria-label="Business card front">
    <div class="front__band">
      <span class="accent accent--left"></span>
      <div class="front__mark">
        <p class="front__logo">LOGO</p>
        <p class="front__service"><span class="hours">24</span>hour Knuckleboom Service</p>
      </div>
    </div>
    <div class="front__body">
      <h1 class="company">HARBOR <span class="hl">LIFT HAULERS, INC.</span></h1>
      <p class="web">www.hlhaulers.com</p>
      <div class="contacts">
        <div class="contacts__col">
          <div class="contacts__row">
            <svg width="9" height="12" viewBox="0 0 9 12"><path d="M4.5 0A4.5 4.5 0 0 0 0 4.5C0 8 4.5 12 4.5 12S9 8 9 4.5A4.5 4.5 0 0 0 4.5 0zm0 6.2a1.7 1.7 0 1 1 0-3.4 1.7 1.7 0 0 1 0 3.4z" fill="#d07712"/></svg>
            <p>428 westcott ave<br>merrick, ny 11542<br>direct - 1 888 lift hauls</p>
          </div>
        </div>
        <div class="contacts__col">
          <div class="contacts__row phone">
            <svg width="9" height="9" viewBox="0 0 9 9"><rect width="9" height="9" rx="1.5" fill="#d07712"/></svg>
            <p>516 487 3091</p>
          </div>
          <div class="contacts__row">
            <svg width="9" height="7" viewBox="0 0 9 7"><rect width="9" height="7" fill="#d07712"/><path d="M0 0l4.5 4L9 0" stroke="#fff" fill="none"/></svg>
            <p>mark@hlhaulers.com</p>
          </div>
        </div>
        <div class="contacts__col">
          <p>you can call me anytime 24/7 to<br>discuss...my cell # is: 516 759 2036</p>
        </div>
      </div>
    </div>
    <span class="accent accent--right"></span>
  </section>

  <section class="card card--back" aria-label="Business card back">
    <span class="accent accent--left"></span>
    <div class="back__content">
      <p class="back__logo">LOGO</p>
      <p class="slogan">OUR LOADS KEEP <span class="hl">ROLLIN</span></p>
      <p class="web">www.hlhaulers.com</p>
    </div>
    <span class="accent accent--right"></span>
  </section>

</body>
</html>
```